2 Fold Brochure

We are a spa looking to create a professional elegant two fold brochure for a spa mainly black and white with a splash of lime green.
Look and feel: chic, modern, and spa-ish.

The front will include an image and also it should say: (somewhere under the photo) wherever you think it will look nice.
Skin Tightening
Cellulite Reduction
Body Contouring

The second Page:
Bipolar Radiofrequency(bolded): for immediate face lifting, tone and a complete new younger looking skin!
Multipolar Radiofrequency(bolded): with Vacuum system for body contour, cellulite and fat detachment from adipose tissue.
Cavitation with red LED to treat face and small areas of the body. Red LED light stimulates collagen synthesis.

Ultra Cavitation will sculpt, treat fat, cellulite and improve body shape! It does NOT involve surgery. There is no need for anesthesia, hospital stay or time off from work. Ultra cavitation will promote microscopic air bubbles to surround the lipocyte(fat cell) membranes and with its resonant frequency, the bubbles cause a high enough pressure to break up fat instantly. These broken lipocytes are then safely metabolized out of the human body.

PRESSOTHERAPY: A Complete Body Detox! Pressortherapy based on air pressure, promotes lymphatic drainage. It aslo has infrared system for body heat and electro muscle stimulation system.

Third Page:
Packages:

1. THE NEW FACELIFT:
*Skin Tightening
*Wrinkle Reduction
*Dark Circle Elimination
*Puffy Eye Relief

BODY SHAPING

2. BODY
*Fat Reduction
*Cellulite Reduction
*Body Firming

3. PRESSOTHERAPY (DETOX) $85
*Toxic Flushing
*Lymphatic Drainage
*Toning

5.POST PREGNANCY
*Fat Reduction
*Tummy Firming and Toning
*Cellulite Reduction
*Butt Toning

Buy 5 get 1 Free - $1,250
Buy 10 get 2 Free- $2,500

The back of the second page will include before and after photos I will be sending later. Also include the Logo in the front and by the prices. I have attached our logo.

Also we need a photo to place in the front. Something that shows face and body fat reduction.

Industry/Entity Type

Hospital

```html
<!DOCTYPE html>
<html lang="en">
<head>
<meta charset="utf-8">
<title>Body Contouring Brochure</title>
<link rel="stylesheet" href="https://fonts.googleapis.com/css2?family=Open+Sans:wght@300;400;600&family=Raleway:wght@400;500;600;700;800&display=swap">
<style>
  :root {
    --bg: #ececec;
    --ink: #111111;
    --text: #555555;
    --muted: #8a8a8a;
    --blue-deep: #0d5c9c;
    --blue-mid: #1f74b8;
    --blue-light: #9fd1f6;
    --blue-letter: #55b3f2;
    --navy: #1a3f73;
    --cream: #f5f4ec;
    --grey-panel: #e4e4e4;
    --white: #ffffff;
    --skin-a: #e9d2c3;
    --skin-b: #f7ece4;
  }
  * { box-sizing: border-box; margin: 0; padding: 0; }
  html, body { width: 1200px; height: 1000px; overflow: hidden; }
  body {
    background: radial-gradient(ellipse at center, #fafafa 0%, var(--bg) 75%);
    font-family: "Open Sans", Arial, sans-serif;
    color: var(--ink);
    position: relative;
  }
  .page-label {
    position: absolute;
    font-family: "Open Sans", Arial, sans-serif;
    font-size: 16px;
    color: #222;
    width: 330px;
    text-align: center;
  }
  .page {
    position: absolute;
    width: 330px;
    height: 430px;
    background: var(--white);
    overflow: hidden;
    box-shadow: 0 6px 18px rgba(0,0,0,0.18);
  }
  .page > svg.page-art { position: absolute; inset: 0; }

  /* ---------- Back cover (page 4) ---------- */
  .back-cover { left: 270px; top: 45px; }
  .logo-lockup {
    position: absolute; left: 20px; top: 178px; width: 250px;
    display: flex; flex-direction: column; align-items: center; gap: 8px;
  }
  .logo-mark {
    width: 62px; height: 62px; border-radius: 50%;
    border: 2px solid var(--ink);
  }
  .logo-name {
    font-family: "Open Sans", Arial, sans-serif;
    font-weight: 600; font-size: 15px; letter-spacing: 1px;
    color: var(--ink);
  }
  .contact-card {
    position: absolute; left: 12px; top: 290px; width: 262px; height: 125px;
    background: var(--white); padding: 18px 14px;
  }
  .contact-row { display: flex; gap: 8px; font-size: 12.5px; line-height: 1.45; color: var(--ink); }
  .contact-row svg { flex: none; margin-top: 2px; }
  .contact-row + .contact-row { margin-top: 14px; }

  /* ---------- Front cover (page 1) ---------- */
  .front-cover { left: 600px; top: 45px; }
  .cover-headlines {
    position: absolute; left: 55px; top: 20px; width: 260px;
    color: var(--white); font-family: "Open Sans", Arial, sans-serif; font-weight: 400;
  }
  .cover-headlines p { font-size: 13px; line-height: 1.9; white-space: nowrap; }
  .cover-headlines p span { font-size: 19px; }
  .cover-headlines .line-2 { padding-left: 4px; }
  .cover-headlines .line-3 { padding-left: 22px; }
  .spine-title {
    position: absolute; left: 40px; top: 415px;
    transform: rotate(-90deg); transform-origin: left top;
    font-family: "Open Sans", Arial, sans-serif; font-size: 21px; font-weight: 400;
    color: var(--ink); white-space: nowrap;
  }

  /* ---------- Inside left (page 2) ---------- */
  .treatments { left: 270px; top: 530px; }
  .treatment { position: absolute; left: 58px; width: 250px; }
  .treatment h3 {
    font-family: "Raleway", Arial, sans-serif; font-size: 10px; line-height: 1.25;
    font-weight: 800; color: var(--navy); letter-spacing: 0.2px;
  }
  .treatment h3 .accent { color: var(--blue-mid); font-weight: 600; font-size: 11px; }
  .treatment p {
    font-family: "Raleway", Arial, sans-serif; font-size: 7px; line-height: 1.45;
    color: var(--muted); margin-top: 8px;
  }
  .treatment p + p { margin-top: 7px; }

  /* ---------- Inside right (page 3) ---------- */
  .packages { left: 600px; top: 530px; }
  .package-badge {
    position: absolute; width: 70px; height: 70px; border-radius: 50%;
    background: var(--white);
    box-shadow: 0 0 0 3px var(--white), 0 2px 8px rgba(0,0,0,0.2);
    display: flex; align-items: center; justify-content: center;
    font-family: "Open Sans", Arial, sans-serif; font-size: 44px; font-weight: 400;
    color: var(--blue-letter);
  }
  .package-badge.ring-right { border-right: 3px solid var(--blue-letter); }
  .package-badge.ring-left { border-left: 3px solid var(--blue-letter); }
  .package { position: absolute; font-family: "Raleway", Arial, sans-serif; }
  .package h3 { font-size: 15px; font-weight: 600; color: var(--ink); white-space: nowrap; }
  .package h3 .accent { color: var(--navy); font-weight: 700; font-size: 17px; }
  .package h3 .soft { color: var(--navy); font-weight: 600; }
  .package ul { list-style: none; margin-top: 5px; }
  .package li { font-size: 7.5px; line-height: 1.6; color: #444; }
  .package-arrow { position: absolute; }
  .pricing {
    position: absolute; left: 38px; top: 385px;
    font-family: "Raleway", Arial, sans-serif; font-size: 8px; font-weight: 800;
    color: var(--navy); line-height: 1.9;
  }
  .pricing .free { color: var(--blue-letter); }
  .pricing .deal { color: var(--ink); }
</style>
</head>
<body>

  <div class="page-label" style="left:270px; top:18px;">Page 4</div>
  <div class="page-label" style="left:600px; top:18px;">Page 1</div>
  <div class="page-label" style="left:270px; top:503px;">Page 2</div>
  <div class="page-label" style="left:600px; top:503px;">Page 3</div>

  <!-- Back cover -->
  <section class="page back-cover">
    <svg class="page-art" width="330" height="430" viewBox="0 0 330 430">
      <rect width="330" height="430" fill="var(--cream)"/>
      <rect x="0" y="0" width="330" height="110" fill="var(--white)"/>
      <path d="M0 0 H215 C245 0 270 50 280 110 V430 H330 V0 Z" fill="var(--ink)"/>
      <path d="M190 0 H222 C250 10 268 60 276 110 L276 430 H270 V130 C262 60 235 15 190 0 Z" fill="var(--blue-light)"/>
      <path d="M0 0 H190 C232 14 258 60 268 118 V0 Z" fill="none"/>
      <rect x="290" y="0" width="18" height="430" fill="var(--grey-panel)"/>
      <rect x="308" y="0" width="22" height="430" fill="var(--ink)"/>
      <g role="img" aria-label="Photo of a woman's face in profile with arrows showing a lifting treatment">
        <defs>
          <linearGradient id="faceTone" x1="0" y1="0" x2="1" y2="1">
            <stop offset="0" stop-color="var(--skin-b)"/>
            <stop offset="1" stop-color="var(--skin-a)"/>
          </linearGradient>
        </defs>
        <path d="M0 0 H188 C230 16 256 62 266 120 L0 120 Z" fill="url(#faceTone)"/>
      </g>
    </svg>
    <div class="logo-lockup">
      <div class="logo-mark"></div>
      <div class="logo-name">Lumea Day Spa</div>
    </div>
    <div class="contact-card">
      <div class="contact-row">
        <svg width="11" height="15" viewBox="0 0 11 15"><path d="M5.5 0C2.5 0 0 2.4 0 5.4 0 9.4 5.5 15 5.5 15S11 9.4 11 5.4C11 2.4 8.5 0 5.5 0Z" fill="var(--blue-mid)"/><circle cx="5.5" cy="5.3" r="2" fill="var(--white)"/></svg>
        <div>1450 Harbor Lane<br>Seacliff, CA 90000<br>555.014.2290</div>
      </div>
      <div class="contact-row">
        <svg width="12" height="12" viewBox="0 0 12 12"><circle cx="6" cy="6" r="5.5" fill="var(--blue-mid)"/><path d="M0.5 6H11.5M6 0.5C3.5 3 3.5 9 6 11.5M6 0.5C8.5 3 8.5 9 6 11.5" stroke="var(--white)" stroke-width="0.8" fill="none"/></svg>
        <div>www.lumeadayspa.com</div>
      </div>
    </div>
  </section>

  <!-- Front cover -->
  <section class="page front-cover">
    <svg class="page-art" width="330" height="430" viewBox="0 0 330 430">
      <defs>
        <linearGradient id="coverBlue" x1="0" y1="0" x2="1" y2="1">
          <stop offset="0" stop-color="var(--blue-mid)"/>
          <stop offset="1" stop-color="var(--blue-deep)"/>
        </linearGradient>
        <linearGradient id="bodyTone" x1="0" y1="0" x2="0" y2="1">
          <stop offset="0" stop-color="var(--skin-b)"/>
          <stop offset="1" stop-color="var(--skin-a)"/>
        </linearGradient>
      </defs>
      <rect width="330" height="430" fill="var(--white)"/>
      <rect x="0" y="0" width="16" height="430" fill="var(--blue-light)"/>
      <rect x="16" y="0" width="30" height="430" fill="var(--grey-panel)"/>
      <path d="M46 0 H330 V150 C250 110 150 115 46 150 Z" fill="url(#coverBlue)"/>
      <path d="M46 150 C150 115 250 110 330 150 V162 C250 124 150 128 46 160 Z" fill="var(--blue-light)"/>
      <path d="M46 160 C150 128 250 124 330 162 V178 C250 140 150 142 46 174 Z" fill="var(--ink)"/>
      <g role="img" aria-label="Photo of a slim waist and hips with a measuring tape">
        <path d="M120 178 C170 150 250 148 300 172 L300 400 L120 400 Z" fill="url(#bodyTone)"/>
      </g>
    </svg>
    <div class="cover-headlines">
      <p class="line-1">Face <span>Lifting</span></p>
      <p class="line-2">Skin <span>Tightening</span></p>
      <p class="line-3">Cellulite <span>Reduction</span></p>
    </div>
    <div class="spine-title">Body Contouring</div>
  </section>

  <!-- Inside left -->
  <section class="page treatments">
    <svg class="page-art" width="330" height="430" viewBox="0 0 330 430">
      <rect width="330" height="430" fill="var(--white)"/>
      <rect x="0" y="0" width="14" height="430" fill="var(--ink)"/>
      <rect x="14" y="0" width="32" height="430" fill="var(--blue-light)"/>
      <path d="M46 32 L53 38 L46 44 Z" fill="var(--white)"/>
      <path d="M46 120 L53 126 L46 132 Z" fill="var(--white)"/>
      <path d="M46 340 L53 346 L46 352 Z" fill="var(--white)"/>
      <path d="M280 430 C300 400 318 380 330 372 V430 Z" fill="var(--grey-panel)"/>
    </svg>
    <article class="treatment" style="top:30px;">
      <h3>BIPOLAR<br><span class="accent">RADIOFREQUENCY</span></h3>
      <p>For immediate face lifting, tone and a complete new younger looking skin!</p>
    </article>
    <article class="treatment" style="top:118px;">
      <h3>MULTIPOLAR<br><span class="accent">RADIOFREQUENCY</span></h3>
      <p>With Vacuum system for body contour, cellulite and fat detachment from adipose tissue.<br>Cavitation with red LED to treat face and small areas of the body. Red LED light stimulates collagen synthesis.</p>
      <p>Ultra Cavitation will sculpt, treat fat, cellulite and improve body shape! It does NOT involve surgery. There is no need for anesthesia, hospital stay or time off from work. Ultra cavitation will promote microscopic air bubbles to surround the lipocyte(fat cell) membranes and with its resonant frequency, the bubbles cause a high enough pressure to break up fat instantly. These broken lipocytes are then safely metabolized out of the human body.</p>
    </article>
    <article class="treatment" style="top:340px;">
      <h3><span class="accent">PRESSOTHERAPY</span></h3>
      <p style="margin-top:5px;">A Complete Body Detox! Pressotherapy based on air pressure, promotes lymphatic drainage. It also has infrared system for body heat and electro muscle stimulation system.</p>
    </article>
  </section>

  <!-- Inside right -->
  <section class="page packages">
    <svg class="page-art" width="330" height="430" viewBox="0 0 330 430">
      <rect width="330" height="430" fill="var(--white)"/>
      <rect x="0" y="0" width="10" height="430" fill="var(--ink)"/>
      <rect x="10" y="0" width="18" height="430" fill="var(--blue-light)"/>
      <path d="M270 430 C295 395 315 375 330 366 V430 Z" fill="var(--grey-panel)"/>
    </svg>

    <div class="package-badge ring-right" style="left:22px; top:20px;">A</div>
    <svg class="package-arrow" style="left:100px; top:44px;" width="18" height="16" viewBox="0 0 18 16"><path d="M2 2 C2 9 6 11 13 11" stroke="var(--blue-letter)" stroke-width="2.5" fill="none"/><path d="M11 6 L16 11 L11 15" stroke="var(--blue-letter)" stroke-width="2.5" fill="none"/></svg>
    <div class="package" style="left:122px; top:22px;">
      <h3>The New <span class="accent">Facelift</span></h3>
      <ul><li>Skin Tightening</li><li>Wrinkle Reduction</li><li>Dark Circle Elimination</li><li>Puffy Eye Relief</li></ul>
    </div>

    <div class="package-badge ring-right" style="left:240px; top:118px;">B</div>
    <svg class="package-arrow" style="left:215px; top:142px;" width="18" height="16" viewBox="0 0 18 16"><path d="M16 2 C16 9 12 11 5 11" stroke="var(--blue-letter)" stroke-width="2.5" fill="none"/><path d="M7 6 L2 11 L7 15" stroke="var(--blue-letter)" stroke-width="2.5" fill="none"/></svg>
    <div class="package" style="left:40px; top:118px;">
      <h3>Body <span class="soft">&nbsp;Shaping</span></h3>
      <ul><li>Fat Reduction</li><li>Cellulite Reduction</li><li>Body Firming</li></ul>
    </div>

    <div class="package-badge ring-right" style="left:22px; top:210px;">C</div>
    <svg class="package-arrow" style="left:100px; top:232px;" width="18" height="16" viewBox="0 0 18 16"><path d="M2 2 C2 9 6 11 13 11" stroke="var(--blue-letter)" stroke-width="2.5" fill="none"/><path d="M11 6 L16 11 L11 15" stroke="var(--blue-letter)" stroke-width="2.5" fill="none"/></svg>
    <div class="package" style="left:122px; top:210px;">
      <h3 style="font-size:13px;">Pressotherapy <span class="soft">(Detox)</span></h3>
      <ul><li>Toxic Flushing</li><li>Lymphatic Drainage</li><li>Toning</li></ul>
    </div>

    <div class="package-badge ring-right" style="left:240px; top:300px;">D</div>
    <svg class="package-arrow" style="left:215px; top:326px;" width="18" height="16" viewBox="0 0 18 16"><path d="M16 2 C16 9 12 11 5 11" stroke="var(--blue-letter)" stroke-width="2.5" fill="none"/><path d="M7 6 L2 11 L7 15" stroke="var(--blue-letter)" stroke-width="2.5" fill="none"/></svg>
    <div class="package" style="left:40px; top:300px;">
      <h3>Post <span class="accent">Pregnancy</span></h3>
      <ul><li>Fat Reduction</li><li>Tummy Firming and Toning</li><li>Cellulite Reduction</li><li>Butt Toning</li></ul>
    </div>

    <div class="pricing">
      <div>GOLD PACKAGE <span class="deal">- BUY 5 GET 1 <span class="free">FREE</span> - $1,250</span></div>
      <div>PLATINUM PACKAGE <span class="deal">- BUY 10 GET 2 <span class="free">FREE</span>- $2,500</span></div>
    </div>
  </section>

</body>
</html>
```